Outsourced Accounting Services - images Brightpane Ad Circuits (BAC) ads needed

I am looking for graphic designer who has experienced in creating images for Brightpane Ad Circuits (BAC) ads.

IMPORTANT NOTES:
Designer has to provide total 27 image dimensions and also the editable artwork file in AI format.

The design created has to be professional and be able to grab attention visually. The message on the ad also has to be clear.

OVERVIEW:
Client is in the business of providing corporate services in Singapore.
They are targeting businesses to take up their Outsourced Accounting Services.
You may find out more info for this service at https://www.ledgerharbourhub.example/outsourced-accounting-services/

Kindly find below the information of the image dimension required, file formats and file size.

==========================================
File Formats: GIF, JPG, PNG
Max. size :150KB

Ad sizes:
200 × 200 Small square
240 × 400 Vertical rectangle
250 × 250 Square
250 × 360 Triple widescreen
300 × 250 Inline rectangle
336 × 280 Large rectangle
580 × 400 Netboard
120 × 600 Skyscraper
160 × 600 Wide skyscraper
300 × 600 Half-page ad
300 × 1050 Portrait
468 × 60 Banner
728 × 90 Leaderboard
930 × 180 Top banner
970 × 90 Large leaderboard
970 × 250 Billboard
980 × 120 Panorama

Target Market(s)

The objective of the ad is to attract the attention of business owners or key decision makers who are looking to enjoy cost savings + achieve professional accounting function through Outsourced Accounting Services (instead of having a in-house accounting team).

Industry/Entity Type

Accounting

Font styles to use
Sans Serif
Other font styles liked:
• roboto

Colors

Designer to choose colors to be used in the design.

Requirements
Must have
• Well thought-out and crafted design to communicate ideas to targeted audience.
Should not have
• 1) No cartoon or cute or funny designs.
• 2) No funny text
• 3) No red / pink / purple colour

```html
<!DOCTYPE html>
<html lang="en">
<head>
<meta charset="utf-8">
<title>Outsourced Accounting Ad Set</title>
<link href="https://fonts.googleapis.com/css2?family=Saira+Semi+Condensed:wght@500;600&display=swap" rel="stylesheet">
<style>
  :root {
    --page: #ffffff;
    --blue-deep: #2f7fe6;
    --blue-mid: #3f9cf0;
    --blue-light: #4fb0f7;
    --text: #ffffff;
    --button: #f4f6f8;
    --button-text: #1d2433;
    --mark: #1646c8;
  }
  * { box-sizing: border-box; margin: 0; padding: 0; }
  html, body { width: 1200px; height: 1200px; overflow: hidden; background: var(--page); }
  body { position: relative; font-family: "Saira Semi Condensed", "Roboto Condensed", sans-serif; color: var(--text); }

  .ad {
    position: absolute;
    background: linear-gradient(135deg, var(--blue-mid), var(--blue-light));
    display: flex; flex-direction: column; align-items: center; justify-content: center;
    text-align: center; overflow: hidden;
  }
  .ad--deep { background: linear-gradient(135deg, var(--blue-deep), var(--blue-mid)); }

  .ad__headline { font-weight: 600; font-size: var(--h); line-height: 1.3; letter-spacing: 0.01em; white-space: nowrap; }
  .ad__sub { font-weight: 500; font-size: var(--s); line-height: 1.5; margin-top: var(--gap, 4px); }
  .ad__button {
    background: var(--button); color: var(--button-text); font-weight: 500;
    font-size: var(--b); line-height: 1.4; border-radius: 999px; padding: 0.25em 1.9em; margin-top: var(--gap, 6px);
    white-space: nowrap;
  }
  .ad__brand {
    display: flex; align-items: center; gap: 0.35em; font-weight: 500;
    font-size: var(--l); line-height: 1; color: var(--text); white-space: nowrap; margin-top: var(--gap, 6px);
    text-align: left; text-transform: uppercase; letter-spacing: 0.04em;
  }
  .ad__brand::before { content: ""; width: 1.9em; height: 1.9em; background: var(--mark); display: block; flex: none; }
  .ad__brand--corner { position: absolute; right: var(--cr, 14px); bottom: var(--cb, 8px); margin: 0; }
  .ad__button--corner { position: absolute; margin: 0; }
  .big { font-size: 1.75em; }
</style>
</head>
<body>

<!-- leaderboard 728x90 -->
<div class="ad ad--deep" style="left:158px;top:29px;width:582px;height:53px;align-items:flex-start;padding-left:10px;--h:18px;--s:10px;--b:7px;--l:6px">
  <p class="ad__headline">Save Up to 79% on Salaries with Outsourced Accounting</p>
  <p class="ad__sub" style="margin-top:0">Chiropractor Further Related Saving on Training, Office Space and Administrative Overhead</p>
  <span class="ad__brand ad__brand--corner" style="top:7px;bottom:auto;--cr:14px">Meridane<br>Consulting</span>
  <span class="ad__button ad__button--corner" style="right:3px;bottom:3px">Learn More</span>
</div>

<!-- top banner 930x180 -->
<div class="ad ad--deep" style="left:162px;top:107px;width:558px;height:107px;justify-content:flex-start;padding-top:20px;--h:20px;--s:10px;--b:7px;--l:8px">
  <p class="ad__headline">Save Up to 79% on Salaries with Outsourced Accounting</p>
  <p class="ad__sub">Chiropractor Further Related Saving on Training, Office Space and Administrative Overhead</p>
  <span class="ad__button" style="margin-top:14px">Learn More</span>
  <span class="ad__brand ad__brand--corner" style="--cr:56px;--cb:12px">Meridane<br>Consulting</span>
</div>

<!-- banner 468x60 -->
<div class="ad" style="left:162px;top:240px;width:438px;height:54px;align-items:flex-start;justify-content:flex-start;padding:2px 0 0 9px;--h:14px;--s:7px;--b:5px;--l:6px">
  <p class="ad__headline">Save Up to 79% on Salaries with Outsourced Accounting</p>
  <p class="ad__sub" style="margin:0 0 0 20px">Chiropractor Further Related Saving on Training, Office Space and Administrative Overhead</p>
  <span class="ad__button ad__button--corner" style="left:171px;bottom:5px">Learn More</span>
  <span class="ad__brand ad__brand--corner" style="--cr:60px;--cb:4px">Meridane<br>Consulting</span>
</div>

<!-- vertical rectangle 240x400 -->
<div class="ad" style="left:157px;top:328px;width:150px;height:216px;--h:15px;--s:10px;--b:9px;--l:8px;--gap:5px">
  <p class="ad__headline">Save Up to 79% on<br>Salaries with<br>Outsourced<br>Accounting Service</p>
  <p class="ad__sub" style="line-height:1.6">Chiropractor Further Related<br>Saving on Training, Office<br>Space and Administrative<br>Overhead</p>
  <span class="ad__button" style="padding:0.3em 2.4em">Learn More</span>
  <span class="ad__brand" style="margin-top:4px">Meridane<br>Consulting</span>
</div>

<!-- square 250x250 -->
<div class="ad" style="left:333px;top:328px;width:150px;height:150px;--h:12px;--s:7px;--b:7px;--l:7px;--gap:2px">
  <p class="ad__headline" style="line-height:1.6">Save Up to 79% on<br>Salaries with Outsourced<br>Accounting Service</p>
  <p class="ad__sub" style="margin-top:0">Chiropractor Further Related Saving<br>on Training, Office Space and<br>Administrative Overhead</p>
  <span class="ad__button" style="margin-top:4px;padding:0.25em 2.2em">Learn More</span>
  <span class="ad__brand" style="margin-top:4px">Meridane<br>Consulting</span>
</div>

<!-- small square 200x200 -->
<div class="ad" style="left:348px;top:509px;width:120px;height:119px;--h:9px;--s:7px;--b:6px;--l:5px;--gap:1px">
  <p class="ad__headline" style="line-height:1.6">Save Up to 79% on<br>Salaries with Outsourced<br>Accounting Service</p>
  <p class="ad__sub" style="margin-top:0;line-height:1.45">Chiropractor Further Related<br>Saving on Training, Office Space<br>and Administrative Overhead</p>
  <span class="ad__button" style="padding:0.2em 2.2em">Learn More</span>
  <span class="ad__brand" style="margin-top:3px">Meridane<br>Consulting</span>
</div>

<!-- half page 300x600 -->
<div class="ad" style="left:510px;top:328px;width:180px;height:360px;--h:21px;--s:14px;--b:13px;--l:10px;--gap:12px">
  <p class="ad__headline" style="line-height:1.45">Save Up to 79%<br>on Salaries with<br>Outsourced<br>Accounting<br>Service</p>
  <p class="ad__sub" style="margin-top:2px;line-height:1.9">Chiropractor Further<br>Related Saving on Training<br>Office Space and<br>Administrative Overhead</p>
  <span class="ad__button" style="padding:0.35em 2.8em">Learn More</span>
  <span class="ad__brand" style="margin-top:8px">Meridane<br>Consulting</span>
</div>

<!-- portrait 300x1050 -->
<div class="ad" style="left:767px;top:38px;width:210px;height:630px;--h:28px;--s:21px;--b:16px;--l:14px;--gap:24px">
  <p class="ad__headline" style="line-height:1.45"><span class="big">Save</span> Up<br>to 79% on<br>Salaries with<br>Outsourced<br>Accounting<br>Service</p>
  <p class="ad__sub" style="margin-top:14px">Chiropractor<br>Further Related<br>Saving on Training,<br>Office Space and<br>Administrative<br>Overhead</p>
  <span class="ad__button" style="padding:0.55em 2.8em">Learn More</span>
  <span class="ad__brand">Meridane<br>Consulting</span>
</div>

<!-- triple widescreen 250x360 -->
<div class="ad" style="left:157px;top:598px;width:143px;height:240px;--h:13px;--s:11px;--b:11px;--l:9px;--gap:10px">
  <p class="ad__headline" style="line-height:1.6">Save Up to 79% on<br>Salaries with<br>Outsourced<br>Accounting Service</p>
  <p class="ad__sub" style="margin-top:6px">Chiropractor Further<br>Related Saving on Training,<br>Office Space and<br>Administrative Overhead</p>
  <span class="ad__button" style="padding:0.35em 2.2em">Learn More</span>
  <span class="ad__brand">Meridane<br>Consulting</span>
</div>

<!-- inline rectangle 300x250 -->
<div class="ad" style="left:315px;top:668px;width:180px;height:150px;--h:13px;--s:7px;--b:7px;--l:7px;--gap:4px">
  <p class="ad__headline">Save Up to 79% on<br>Salaries with Outsourced<br>Accounting Service</p>
  <p class="ad__sub" style="margin-top:8px;line-height:1.7">Chiropractor Further Related Saving on<br>Training, Office Space and Administrative<br>Overhead</p>
  <span class="ad__button" style="padding:0.25em 2.2em">Learn More</span>
  <span class="ad__brand" style="margin-top:4px">Meridane<br>Consulting</span>
</div>

<!-- large rectangle 336x280 -->
<div class="ad" style="left:510px;top:734px;width:202px;height:168px;justify-content:flex-start;padding-top:14px;--h:14px;--s:7px;--b:8px;--l:7px">
  <p class="ad__headline" style="line-height:1.45">Save Up to 79% on<br>Salaries with Outsourced<br>Accounting Service</p>
  <p class="ad__sub" style="margin-top:10px;line-height:1.7">Chiropractor Further Related Saving on<br>Training, Office Space and Administrative<br>Overhead</p>
  <span class="ad__button ad__button--corner" style="left:14px;bottom:10px">Learn More</span>
  <span class="ad__brand ad__brand--corner" style="--cr:18px;--cb:12px">Meridane<br>Consulting</span>
</div>

<!-- netboard 580x400 -->
<div class="ad" style="left:720px;top:698px;width:348px;height:240px;justify-content:flex-start;padding-top:10px;--h:25px;--s:13px;--b:12px;--l:11px">
  <p class="ad__headline" style="line-height:1.3">Save Up to 79% on<br>Salaries with Outsourced<br>Accounting Service</p>
  <p class="ad__sub" style="margin-top:14px;line-height:1.7">Chiropractor Further Related Saving on Training,<br>Office Space and Administrative Overhead</p>
  <span class="ad__button ad__button--corner" style="left:66px;bottom:20px;padding:0.3em 2.6em">Learn More</span>
  <span class="ad__brand ad__brand--corner" style="--cr:46px;--cb:24px">Meridane<br>Consulting</span>
</div>

<!-- small leaderboard -->
<div class="ad ad--deep" style="left:207px;top:864px;width:282px;height:36px;justify-content:flex-start;padding-top:3px;--h:8px;--s:4px;--b:4px;--l:4px">
  <p class="ad__headline">Save Up to 79% on Salaries with Outsourced Accounting</p>
  <p class="ad__sub" style="margin-top:0">Chiropractor Further Related Saving on Training, Office Space and Administrative Overhead</p>
  <span class="ad__button ad__button--corner" style="left:116px;bottom:4px">Learn More</span>
  <span class="ad__brand ad__brand--corner" style="--cr:48px;--cb:3px">Meridane<br>Consulting</span>
</div>

<!-- large leaderboard 970x90 -->
<div class="ad" style="left:138px;top:927px;width:588px;height:71px;justify-content:flex-start;padding-top:3px;--h:19px;--s:10px;--b:8px;--l:7px">
  <p class="ad__headline">Save Up to 79% on Salaries with Outsourced Accounting</p>
  <p class="ad__sub" style="margin-top:0">Chiropractor Further Related Saving on Training, Office Space and Administrative Overhead</p>
  <span class="ad__button ad__button--corner" style="left:251px;bottom:4px">Learn More</span>
  <span class="ad__brand ad__brand--corner" style="--cr:12px;--cb:5px">Meridane<br>Consulting</span>
</div>

<!-- billboard 970x250 -->
<div class="ad" style="left:489px;top:1009px;width:582px;height:149px;justify-content:flex-start;padding-top:26px;--h:21px;--s:12px;--b:13px;--l:9px">
  <p class="ad__headline">Save Up to 79% on Salaries with Outsourced Accounting</p>
  <p class="ad__sub" style="margin-top:14px">Chiropractor Further Related Saving on Training, Office Space and Administrative Overhead</p>
  <span class="ad__button ad__button--corner" style="left:226px;bottom:13px;padding:0.35em 2.6em">Learn More</span>
  <span class="ad__brand ad__brand--corner" style="--cr:46px;--cb:20px">Meridane<br>Consulting</span>
</div>

</body>
</html>
```